Crossword App Main Page Design

For a crossword application we need a main page. I am enclosing the current temporary design. There will be 5 buttons. We want a simple but attractive design. Vector designs are preferred. Thank you very much for your interest.
The name of the application is Polyglyph Gridword Riddle and the motto is "gridplay rebuilt." So please use this name on the screen.
Thwe designs I have received so far almost the same with one I have attached. Only the button colors and background image are different. Please try different placement and buttons.
Thanks

```html
<!DOCTYPE html>
<html lang="en">
<head>
<meta charset="utf-8">
<title>Polyglyph Gridword Riddle — Main Menu</title>
<link rel="stylesheet" href="https://fonts.googleapis.com/css2?family=Nunito:wght@700;800&family=Arimo:wght@700&display=swap">
<style>
  :root {
    --page-bg: #1b1b1b;
    --screen-bg: #111111;
    --screen-glow: #1e1e1e;
    --status-bg: #000000;
    --status-text: #e6e6e6;
    --header-top: #c27444;
    --header-bottom: #93502a;
    --header-edge: #6b3617;
    --title-text: #f7efe4;
    --motto-text: #f1dcc6;
    --gear: #d9d9d9;
    --label: #ffffff;

    --red-top: #ea3f45;
    --red-bottom: #c30c14;
    --red-edge: #ff5a60;
    --orange-top: #f7a83e;
    --orange-bottom: #ee6804;
    --orange-edge: #ffb651;
    --green-top: #a2de33;
    --green-bottom: #72bd00;
    --green-edge: #b6ef50;
    --teal-top: #33d7a6;
    --teal-bottom: #04a970;
    --teal-edge: #52edbb;
    --purple-top: #9364dc;
    --purple-bottom: #5619c2;
    --purple-edge: #a57cf0;
  }

  html, body {
    margin: 0;
    width: 1200px;
    height: 900px;
    overflow: hidden;
    background: var(--page-bg);
  }

  .app-screen {
    position: absolute;
    left: 354px;
    top: 13px;
    width: 492px;
    height: 874px;
    background: radial-gradient(ellipse at 50% 45%, var(--screen-glow), var(--screen-bg) 75%);
    overflow: hidden;
    font-family: "Nunito", sans-serif;
  }

  .status-bar {
    height: 27px;
    background: var(--status-bg);
    color: var(--status-text);
    font-family: "Arimo", sans-serif;
    font-size: 17px;
    font-weight: 700;
    display: flex;
    align-items: center;
    justify-content: space-between;
    padding: 0 8px;
    box-sizing: border-box;
  }
  .status-carrier { display: flex; align-items: center; gap: 4px; }
  .status-bar svg { display: block; }

  .title-bar {
    position: relative;
    height: 90px;
    background: linear-gradient(var(--header-top), var(--header-bottom));
    border-bottom: 3px solid var(--header-edge);
    box-sizing: border-box;
  }
  .brand {
    position: absolute;
    left: 0;
    right: 0;
    top: 14px;
    text-align: center;
  }
  .app-name {
    margin: 0;
    color: var(--title-text);
    font-size: 24px;
    font-weight: 800;
    line-height: 32px;
    white-space: nowrap;
  }
  .app-motto {
    margin: 2px 0 0;
    color: var(--motto-text);
    font-size: 15px;
    font-weight: 700;
    line-height: 20px;
  }
  .settings-gear {
    position: absolute;
    right: 16px;
    top: 23px;
  }

  .menu {
    list-style: none;
    margin: 0;
    padding: 0;
  }
  .menu-button {
    position: absolute;
    left: 63px;
    width: 370px;
    height: 99px;
    border-radius: 8px;
    border: 3px solid var(--edge);
    box-sizing: border-box;
    background:
      linear-gradient(rgba(255,255,255,0.16), rgba(255,255,255,0.06) 50%, rgba(0,0,0,0) 52%),
      linear-gradient(var(--top), var(--bottom));
    box-shadow: 0 6px 10px rgba(0,0,0,0.6);
    color: var(--label);
    font-size: 36px;
    font-weight: 700;
    display: flex;
    align-items: center;
    justify-content: center;
    text-shadow: 0 2px 2px rgba(0,0,0,0.25);
  }
  .menu-button.play   { top: 178px; font-size: 40px; --top: var(--red-top); --bottom: var(--red-bottom); --edge: var(--red-edge); }
  .menu-button.mine   { top: 306px; --top: var(--orange-top); --bottom: var(--orange-bottom); --edge: var(--orange-edge); }
  .menu-button.shop   { top: 433px; --top: var(--green-top); --bottom: var(--green-bottom); --edge: var(--green-edge); }
  .menu-button.about  { top: 561px; --top: var(--teal-top); --bottom: var(--teal-bottom); --edge: var(--teal-edge); }
  .menu-button.config { top: 688px; --top: var(--purple-top); --bottom: var(--purple-bottom); --edge: var(--purple-edge); }
</style>
</head>
<body>
  <main class="app-screen">
    <div class="status-bar">
      <span class="status-carrier">
        <svg width="24" height="12" viewBox="0 0 24 12" aria-hidden="true">
          <rect x="0" y="9" width="3" height="3" fill="currentColor"/>
          <rect x="5" y="7" width="3" height="5" fill="currentColor"/>
          <rect x="10" y="5" width="3" height="7" fill="currentColor"/>
          <rect x="15" y="2" width="3" height="10" fill="currentColor"/>
          <rect x="20" y="0" width="3" height="12" fill="currentColor"/>
        </svg>
        CARRIER
      </span>
      <svg width="14" height="17" viewBox="0 0 14 17" aria-label="Locked">
        <path d="M3 8V5a4 4 0 0 1 8 0v3" fill="none" stroke="currentColor" stroke-width="2"/>
        <rect x="1" y="8" width="12" height="9" rx="1" fill="currentColor"/>
      </svg>
      <svg width="30" height="14" viewBox="0 0 30 14" aria-label="Battery">
        <rect x="1" y="1" width="25" height="12" rx="2" fill="none" stroke="currentColor" stroke-width="1.5"/>
        <rect x="3" y="3" width="21" height="8" fill="currentColor"/>
        <rect x="27" y="4.5" width="2.5" height="5" fill="currentColor"/>
      </svg>
    </div>

    <header class="title-bar">
      <div class="brand">
        <h1 class="app-name">Polyglyph Gridword Riddle</h1>
        <p class="app-motto">gridplay rebuilt.</p>
      </div>
      <svg class="settings-gear" width="44" height="44" viewBox="0 0 44 44" aria-label="Settings">
        <circle cx="22" cy="22" r="17" fill="none" stroke="var(--gear)" stroke-width="7" stroke-dasharray="6.7 6.7"/>
        <circle cx="22" cy="22" r="13" fill="var(--gear)"/>
        <circle cx="22" cy="22" r="5" fill="var(--header-bottom)"/>
      </svg>
    </header>

    <ul class="menu">
      <li class="menu-button play">PLAY</li>
      <li class="menu-button mine">My Puzzles</li>
      <li class="menu-button shop">Buy Puzzles</li>
      <li class="menu-button about">About</li>
      <li class="menu-button config">Settings</li>
    </ul>
  </main>
</body>
</html>
```